Clear Path IT - KJW - March 2018 - Advertisement 1/2 Page

I am looking to get some opinions to streamline this 1/2 page advertisement for our IT company that specializes in the medical industry and clean up and make it pop. I really want to capture the readers attention and stick out in this medical newspaper. I am looking to get some opinions to streamline this 1/2 page advertisement for our IT company that specializes in the medical industry and clean up and make it pop. I really want to capture the readers attention and stick out in this medical newspaper.

Target Market(s)

Medical / Healthcare

Industry/Entity Type

Medical

Colors
9dd4eb
33a6d7
0692cd
0255a3
3277b5
85acd3
ffffff

Requirements
Must have
• Simple and Clean look that is 1/2 page and really catches the practice manager or doctors eyes
Nice to have
• Simple and Clean look that is 1/2 page and really catches the practice manager or doctors eyes. Has the logos for the software companies is a MUST. I attached a medical flyer with the logos on it to use.
Should not have
• Less pictures of doctors

```html
<!DOCTYPE html>
<html lang="en">
<head>
<meta charset="utf-8">
<title>Clear Path IT – Half Page Advertisement</title>
<link rel="stylesheet" href="https://fonts.googleapis.com/css2?family=Arimo:wght@400;700&display=swap">
<style>
  :root {
    --page-bg: #f2f4f7;
    --navy: #02326e;
    --deep-blue: #0255a3;
    --mid-blue: #3277b5;
    --bright-blue: #0692cd;
    --sky-blue: #33a6d7;
    --pale-blue: #9dd4eb;
    --soft-blue: #85acd3;
    --white: #ffffff;
    --badge-grey: #c9d2dc;
  }
  * { margin: 0; padding: 0; box-sizing: border-box; }
  html, body {
    width: 1200px;
    height: 1200px;
    overflow: hidden;
    background: var(--page-bg);
    font-family: "Arimo", Arial, sans-serif;
  }
  .ad {
    position: absolute;
    left: 0;
    top: 180px;
    width: 1200px;
    height: 840px;
    overflow: hidden;
    background: radial-gradient(ellipse at 55% 60%, var(--mid-blue) 0%, var(--deep-blue) 45%, #034a94 100%);
    color: var(--white);
  }
  .brand {
    position: absolute;
    left: 99px;
    top: 100px;
  }
  .brand-name {
    font-size: 72px;
    font-weight: 400;
    letter-spacing: -1px;
    line-height: 1;
  }
  .brand-tagline {
    margin-top: 10px;
    font-size: 15px;
    font-weight: 700;
    letter-spacing: 0.3px;
  }
  .band-light {
    position: absolute;
    left: 0;
    top: 229px;
    width: 1200px;
    height: 188px;
    background: var(--sky-blue);
  }
  .banner {
    position: absolute;
    left: 0;
    top: 244px;
    width: 842px;
    height: 161px;
  }
  .headline {
    position: absolute;
    left: 36px;
    top: 262px;
    font-weight: 700;
    line-height: 1;
    white-space: nowrap;
  }
  .headline-lead {
    font-size: 48px;
    color: var(--white);
  }
  .headline-main {
    margin-top: 14px;
    font-size: 68px;
    color: var(--sky-blue);
    letter-spacing: 0.5px;
  }
  .intro {
    position: absolute;
    left: 41px;
    top: 452px;
    width: 745px;
    font-size: 22px;
    line-height: 28px;
    text-align: justify;
    color: var(--white);
  }
  .contact-list { list-style: none; }
  .contact {
    position: absolute;
    left: 74px;
    display: flex;
    align-items: center;
    gap: 16px;
    font-size: 34px;
    font-weight: 700;
  }
  .contact-phone { top: 586px; }
  .contact-web { top: 636px; }
  .contact svg { width: 40px; height: 40px; }
  .partner-strip {
    position: absolute;
    left: 0;
    top: 709px;
    width: 1200px;
    height: 95px;
    background: var(--white);
    display: flex;
    align-items: center;
    gap: 22px;
    padding-left: 40px;
  }
  .partner-badge {
    height: 56px;
    background: var(--badge-grey);
    border-radius: 4px;
  }
  .partner-badge.wide { width: 100px; }
  .partner-badge.square { width: 56px; background: var(--sky-blue); }
  .partner-badge.round { width: 44px; height: 44px; border-radius: 50%; background: var(--soft-blue); }
  .spokesperson-photo {
    position: absolute;
    left: 820px;
    top: 135px;
    width: 380px;
    height: 705px;
    border-radius: 180px 180px 0 0;
    background: linear-gradient(180deg, #e6d3a3 0%, #d9b98f 28%, #9a9a9e 50%, #7c7c82 100%);
  }
</style>
</head>
<body>
  <main class="ad">
    <div class="brand">
      <div class="brand-name">Clear Path IT</div>
      <div class="brand-tagline">MEDICAL &amp; DENTAL OFFICE TECHNOLOGY SOLUTIONS</div>
    </div>

    <div class="band-light"></div>
    <svg class="banner" viewBox="0 0 842 161" aria-hidden="true">
      <polygon points="0,0 783,0 842,80 783,161 0,161" fill="var(--navy)"/>
    </svg>

    <h1 class="headline">
      <div class="headline-lead">The right medical IT COMPANY</div>
      <div class="headline-main">IT’s not just a DREAM</div>
    </h1>

    <p class="intro">At Clear Path IT, we are experts who have hired experts, so you get an IT guy who’s capable, precise, thorough and knows that communicating with our clients is as important as connecting the right wires. Clear Path IT keeps your office working efficiently with precision.</p>

    <ul class="contact-list">
      <li class="contact contact-phone">
        <svg viewBox="0 0 40 40" aria-hidden="true">
          <circle cx="20" cy="20" r="18" fill="none" stroke="var(--white)" stroke-width="2.5"/>
          <path d="M14 11c1.5-1 2.5-.5 3.3 1l1.6 3c.6 1.1.3 2-.7 2.7l-1 .7c.8 2 2.4 3.7 4.4 4.6l.8-1c.7-1 1.6-1.2 2.7-.6l3 1.6c1.5.8 1.8 1.9.8 3.3-1.6 2.2-4 2.7-6.8 1.3-4.2-2.1-7.4-5.4-9.2-9.7C12.3 15.4 12.4 12.5 14 11z" fill="var(--white)"/>
        </svg>
        800- 555- 0142
      </li>
      <li class="contact contact-web">
        <svg viewBox="0 0 40 40" aria-hidden="true" fill="none" stroke="var(--white)" stroke-width="2.2">
          <circle cx="20" cy="20" r="17"/>
          <ellipse cx="20" cy="20" rx="8" ry="17"/>
          <line x1="3" y1="20" x2="37" y2="20"/>
          <path d="M6 11h28M6 29h28"/>
        </svg>
        clearpathit.com
      </li>
    </ul>

    <div class="partner-strip" aria-label="Technology partner certifications">
      <div class="partner-badge wide"></div>
      <div class="partner-badge square"></div>
      <div class="partner-badge wide"></div>
      <div class="partner-badge wide"></div>
      <div class="partner-badge round"></div>
      <div class="partner-badge wide"></div>
    </div>

    <div class="spokesperson-photo" role="img" aria-label="Photo of a smiling businesswoman in a grey suit with arms crossed"></div>
  </main>
</body>
</html>
```